Business card - house cleaning company

We want friendly high end business card highlighting our services . NO LOGOs on back of card please.. no vertical cards NO DOUBLE BROOMS

2 owners of the company: Corinne Halvey & Joel Brandt

Included phone number: (555)318-2047

Email: brightlanetidy@mailnest.example

Website: www.brightlanetidy.example

Bonded & Insured

Larkspur Ridge, CO 80599

Slogan maybe: Bringing a brighter shine to every corner of home

We want elegant high end card for house cleaning service. Maybe 2 sided if needed. Can it have bullet points of some services we offer

Residential Home Cleaning
Vacation Rental Cleaning
Commercial Cleaning
Carpet Cleaning
Window Cleaning
Property Management
Property Inspections
Property Maintenance
Trash Removal
Concierge Services

Highlight service on back of card. If we can do a one sided card with all this that’s great as well. Not cartoony.

Our logo attached and a design somone I had Perrin but they put very little time in. Not Unique enough. If you can do a custom design with a feminine touch that be great.

You will be eliminated for not reading the brief. NO DOUBLE LOGOS NO DOUBLE BROOMS. PLEASE BE CREATIVE. IF POST SAME LOGO WITH SMAL CHANGES RHEY WILL BE ELIMINATED. BE CREATIVE.

Thank you everyone for your designs. please only use the logo 1 time. and would love to see some that dont look all the same. We appreciate your time.

Target Market(s)

Residential and vacation rental home cleaning maid service

Industry/Entity Type

House cleaning maid services

Contact Information for Business Card

For business card use logo. black and green one provided. others for example. I wil try find some example.. We want friendly high end look. 2 owners of the company: Corinne Halvey & Joel Brandt Included phone number: (555)318-2047 Email: brightlanetidy@mailnest.example Website: www.brightlanetidy.example Bonded & Insured Estes Park, CO Slogan maybe: Bringing a brighter shine to every corner of home or Quality Service Guaranteed We want elegant high end card for house cleaning service. Maybe 2 sided if needed. Can it have bullet points of some services we offer Residential Home Cleaning Vacation Rental Cleaning Commercial Cleaning Carpet Cleaning Window Cleaning Property Management Property Inspections Property Maintenance Trash Removal Concierge Services

Requirements
Must have
• For business card use logo . Creativity. black and green one provided. We want friendly high end look. 2 owners of the company: Corinne Halvey & Joel Brandt Included phone number: (555)318-2047 Email: brightlanetidy@mailnest.example Website: www.brightlanetidy.example Licensed Bonded & Insured Estes Park, CO Slogan maybe: Bringing a brighter shine to every corner of home or Quality Service Guaranteed We want elegant high end card for house cleaning service. Maybe 2 sided if needed. Can it have bullet points of some services we offer Residential Home Cleaning Vacation Rental Cleaning Commercial Cleaning Carpet Cleaning Window Cleaning Property Management Property Inspections Property Maintenance Trash Removal Concierge Services .. creatitivty a plus. whimsical. we like stars..
Nice to have
• we want much better than the example of biz card provided as example. logo has colors that are in our website palette as well. We are open to ideas for the business card design. Will pay tip to best work. PLEASE USE COMPLIMENTING COLORS. . WE LIKE BLACK AND WHITE, stars
Should not have
• NO DOUBLE LOGOS. READ READ. READ. YOU WILL BE ELIMINATED no double logos or double brooms same side of card. I want didfrent examples. please don't make all your submission look the same

```html
<!DOCTYPE html>
<html lang="en">
<head>
<meta charset="utf-8">
<title>Bright Lane Tidy – Business Card</title>
<link href="https://fonts.googleapis.com/css2?family=Arimo:wght@400;700&family=Open+Sans:wght@700&display=swap" rel="stylesheet">
<style>
  :root {
    --page: #2b2b2b;
    --card: #0e0e0e;
    --green: #6f9441;
    --blue: #2f6a9a;
    --white: #f4f4f4;
    --rule: #3a3a3a;
  }
  * { box-sizing: border-box; margin: 0; padding: 0; }
  html, body { width: 1200px; height: 900px; overflow: hidden; }
  body {
    background: var(--page);
    font-family: "Arimo", Arial, sans-serif;
    color: var(--white);
    position: relative;
  }
  .card {
    position: absolute;
    left: 250px;
    width: 700px;
    height: 400px;
    background: var(--card);
    border-radius: 20px;
    overflow: hidden;
  }
  .card--front { top: 40px; }
  .card--back { top: 460px; }

  /* front */
  .brand {
    position: absolute;
    right: 40px;
    top: 92px;
    display: flex;
    align-items: center;
    gap: 12px;
  }
  .brand__dot {
    width: 16px; height: 16px;
    border-radius: 50%;
    background: var(--green);
  }
  .brand__name {
    font-family: "Arimo", Arial, sans-serif;
    font-weight: 700;
    font-size: 38px;
    color: var(--blue);
    letter-spacing: 0.5px;
    white-space: nowrap;
  }
  .rule {
    position: absolute;
    height: 1px;
    background: var(--rule);
  }
  .rule--logo { left: 300px; width: 370px; top: 170px; }
  .rule--names { left: 40px; width: 400px; top: 236px; }
  .owners {
    position: absolute;
    left: 40px;
    top: 198px;
    font-family: "Open Sans", Arial, sans-serif;
    font-weight: 700;
    font-size: 24px;
    color: var(--blue);
    text-transform: uppercase;
    letter-spacing: 0.3px;
    white-space: nowrap;
  }
  .contact {
    position: absolute;
    left: 44px;
    top: 248px;
    list-style: none;
  }
  .contact__item {
    display: flex;
    align-items: center;
    gap: 10px;
    font-size: 17px;
    height: 22px;
    line-height: 22px;
    white-space: nowrap;
  }
  .contact__item svg { width: 16px; height: 16px; flex: none; fill: var(--blue); }
  .credentials {
    position: absolute;
    right: 40px;
    top: 304px;
    font-size: 19px;
    color: var(--green);
    text-transform: uppercase;
    white-space: nowrap;
  }
  .slogan-band {
    position: absolute;
    left: 0; bottom: 0;
    width: 100%;
    height: 52px;
    background: var(--green);
    display: flex;
    align-items: center;
    justify-content: center;
    font-size: 20px;
    text-transform: uppercase;
    color: var(--white);
    letter-spacing: 0.3px;
    white-space: nowrap;
  }

  /* back */
  .services-band {
    position: absolute;
    left: 0; top: 105px;
    width: 100%;
    height: 190px;
    background: var(--green);
    display: flex;
    gap: 40px;
    padding: 22px 0 0 60px;
  }
  .services {
    list-style: none;
  }
  .services__item {
    display: flex;
    align-items: center;
    gap: 10px;
    font-size: 16px;
    text-transform: uppercase;
    height: 30px;
    white-space: nowrap;
  }
  .services__item::before {
    content: "";
    width: 8px; height: 8px;
    border-radius: 50%;
    background: var(--white);
  }
</style>
</head>
<body>
  <section class="card card--front" aria-label="Business card front">
    <div class="brand">
      <span class="brand__dot"></span>
      <span class="brand__name">Bright Lane Tidy</span>
    </div>
    <div class="rule rule--logo"></div>
    <h1 class="owners">Corinne Halvey &amp; Joel Brandt</h1>
    <div class="rule rule--names"></div>
    <ul class="contact">
      <li class="contact__item">
        <svg viewBox="0 0 24 24"><path d="M6.6 10.8a15.1 15.1 0 0 0 6.6 6.6l2.2-2.2a1 1 0 0 1 1-.25 11.4 11.4 0 0 0 3.6.57 1 1 0 0 1 1 1V20a1 1 0 0 1-1 1A17 17 0 0 1 3 4a1 1 0 0 1 1-1h3.5a1 1 0 0 1 1 1c0 1.25.2 2.45.57 3.57a1 1 0 0 1-.25 1z"/></svg>
        (555)318-2047
      </li>
      <li class="contact__item">
        <svg viewBox="0 0 24 24"><path d="M2 5h20v14H2z M4 7v.4l8 5.2 8-5.2V7z" fill-rule="evenodd"/></svg>
        brightlanetidy@mailnest.example
      </li>
      <li class="contact__item">
        <svg viewBox="0 0 24 24"><path d="M12 2a10 10 0 1 0 0 20 10 10 0 0 0 0-20zm0 2c.9 0 2.2 1.9 2.8 5H9.2C9.8 5.9 11.1 4 12 4zM4.3 9h2.9a19 19 0 0 0 0 6H4.3a8 8 0 0 1 0-6zm4.9 0h5.6a17 17 0 0 1 0 6H9.2a17 17 0 0 1 0-6zm7.6 0h2.9a8 8 0 0 1 0 6h-2.9a19 19 0 0 0 0-6zM9.2 17h5.6c-.6 3.1-1.9 5-2.8 5s-2.2-1.9-2.8-5z"/></svg>
        www.brightlanetidy.example
      </li>
      <li class="contact__item">
        <svg viewBox="0 0 24 24"><path d="M12 2a7 7 0 0 0-7 7c0 5.2 7 13 7 13s7-7.8 7-13a7 7 0 0 0-7-7zm0 9.5A2.5 2.5 0 1 1 12 6.5a2.5 2.5 0 0 1 0 5z"/></svg>
        Larkspur Ridge, CO 80599
      </li>
    </ul>
    <p class="credentials">Bonded &amp; Insured</p>
    <p class="slogan-band">Bringing a brighter shine to every corner of home</p>
  </section>

  <section class="card card--back" aria-label="Business card back">
    <div class="services-band">
      <ul class="services">
        <li class="services__item">Residential Home Cleaning</li>
        <li class="services__item">Vacation Rental Cleaning</li>
        <li class="services__item">Commercial Cleaning</li>
        <li class="services__item">Carpet Cleaning</li>
        <li class="services__item">Window Cleaning</li>
      </ul>
      <ul class="services">
        <li class="services__item">Property Management</li>
        <li class="services__item">Property Inspections</li>
        <li class="services__item">Property Maintenance</li>
        <li class="services__item">Trash Removal</li>
        <li class="services__item">Concierge Services</li>
      </ul>
    </div>
  </section>
</body>
</html>
```